Business card design needed

We are a gardening company who handle:
All Forms of gardens work including
Mowing
Pruning
edging
weeding
Poisoning
Landscaping
Minor Stump Removal
Rubbish Removal
and more

I want a card that look professional not cartoon style

Industry/Entity Type

Business

Contact Information for Business Card

Fernhollow Yard and Lawn Service

Greg Halden
0486152938

```html
<!DOCTYPE html>
<html lang="en">
<head>
<meta charset="utf-8">
<title>Fernhollow Yard and Lawn Service – Business Card</title>
<link href="https://fonts.googleapis.com/css2?family=Open+Sans:wght@500;600;700&family=Michroma&display=swap" rel="stylesheet">
<style>
  :root {
    --backdrop: #2e2e2e;
    --card: #ffffff;
    --leaf: #6cbd45;
    --text-light: #ffffff;
  }
  * { margin: 0; padding: 0; box-sizing: border-box; }
  html, body {
    width: 1200px;
    height: 1000px;
    overflow: hidden;
    background: var(--backdrop);
  }
  .business-card {
    position: absolute;
    left: 167px;
    top: 257px;
    width: 864px;
    height: 469px;
    background: var(--card);
    font-family: "Open Sans", sans-serif;
  }
  .brand-band {
    position: absolute;
    left: 0;
    top: 102px;
    width: 552px;
    height: 122px;
    background: var(--leaf);
  }
  .brand-name {
    position: absolute;
    left: 29px;
    top: 42px;
    color: var(--text-light);
    font-size: 28px;
    font-weight: 600;
    white-space: nowrap;
    line-height: 1;
  }
  .accent-block {
    position: absolute;
    left: 763px;
    top: 102px;
    width: 101px;
    height: 122px;
    background: var(--leaf);
  }
  .contact {
    position: absolute;
    left: 578px;
    top: 131px;
    width: 180px;
    color: var(--leaf);
  }
  .contact-name {
    font-size: 31px;
    font-weight: 600;
    letter-spacing: -0.2px;
    line-height: 1;
    white-space: nowrap;
  }
  .contact-phone {
    margin-top: 7px;
    font-size: 17px;
    font-weight: 700;
    line-height: 21px;
  }
  .services {
    position: absolute;
    left: 18px;
    top: 402px;
    list-style: none;
    display: grid;
    grid-template-columns: 244px 231px 200px;
    grid-auto-flow: column;
    grid-template-rows: repeat(3, 18px);
    color: var(--leaf);
    font-family: "Michroma", sans-serif;
    font-size: 9.5px;
    letter-spacing: 1.6px;
    text-transform: uppercase;
    white-space: nowrap;
  }
</style>
</head>
<body>
  <main class="business-card">
    <div class="brand-band">
      <h1 class="brand-name">Fernhollow Yard and Lawn Service</h1>
    </div>
    <div class="accent-block"></div>
    <section class="contact">
      <p class="contact-name">Greg Halden</p>
      <p class="contact-phone">Phone:<br>0486152938</p>
    </section>
    <ul class="services">
      <li>-Mowing</li>
      <li>-Weeding</li>
      <li>-Minor Stump Removal</li>
      <li>-Pruning</li>
      <li>-Poisoning</li>
      <li>-Rubbish Removal</li>
      <li>-Edging</li>
      <li>-Landscaping</li>
      <li>-And More</li>
    </ul>
  </main>
</body>
</html>
```